The Wrenfield New Flyer & Advert Design Project

Portrait rack card specs:
double sided
minimum 250 dpi, 350 preferred
> PDF output preferred
> 105mm wide
> 216mm high
> measurements include 3mm BLEED and must include a 3mm print buffer/border

Landscape advert specs:
Single sided
166mm (w) x 117mm (h) with no bleed or crop marks please.

Please check out our website and socials for inspiration.
https://www.thewrenfieldtasmania.example.com.au
Facebook/Instagram - thewrenfieldtas

Brand Summary — The Wrenfield Tasmania
Vibe & Identity:
Eco-luxury meets wild-Tasmanian beauty: natural materials, clean air, panoramic coastal/mountain views, barefoot-by-the-sea meets curated comfort.
A retreat that feels upscale yet warm — elegant pods + relaxed seaside/river/mountain eco-luxe charm.
Location & Setting:
Perched on Mount Halbrook with breathtaking views overlooking the Corvin River, Bass Strait and surrounds.
Surrounded by native bush, with access to nearby MTB trails, coastlines, and wilderness — a sanctuary in nature yet within 10 minutes of amenities.
What Guests Experience:
Stylish eco-luxe pod accommodation with modern comforts + large windows framing sunset/sunrise over sea and river.
A weekend café & bar serving Tasmanian produce, craft beverages and sharing-plate style dining.
Proximity to outdoor adventure: MTB trails, coastal hikes, water activities; ideal for relaxation & adventure alike.
A basecamp for exploring Northern Tasmania — from wineries and heritage towns to wild beaches and forests.
Mood & Tone for Design:
Calm, refined, natural — think earthy tones, textured backgrounds, relaxed yet polished typography.
Elements of bohemian style (raw linen textures, hand-drawn or rustic icons, soft light, organic shapes) balanced with luxe minimalism (clean lines, elegant spacing, refined layout).
Sense of escape, stillness, nature, horizon — visuals that evoke sky, water, bushland, wide open space, serenity, and understated luxury.
Key Messages (to highlight):
Eco-luxe pods on Mount Halbrook with panoramic sea & river views
100% Tasmanian café & bar — local produce, crafted for you
Adventure & nature on your doorstep — MTB trails, hiking, coastlines, Northern Tasmania exploration base
A unique blend: luxury comfort + raw Tasmanian wilderness
🎨 Suggested Design Directions
Colour palette: earth tones (soft greens, sandstone, muted blues, warm neutrals), accent with subtle bronze or copper highlights for a luxe touch.
Textures & Visuals: use wood grain, rusticated paper or linen backgrounds; overlay with soft, dreamy photos of sea/river/mountain views; silhouettes of Tasmanian bush or trails.
Imagery focus: pods at sunrise/sunset, views of sea + river + mountain, silhouette of rider/hiker, warm café ambience, local produce — capturing both serenity and adventure.
Layout feel: breathing space, minimal clutter — maybe one large landscape photo at top or bottom, subtle framing or vignette effect, balanced white/negative space, easy-to-scan copy.

Please feel free to ask me for more images. Problem at the moment is site is still under construction, interior shots will be available in 2 weeks, pods open from mid-January 2026 and cafe bar opens mid-February 2026

Target Market(s)

Eco-luxe travelers and Mountain Bike enthusiasts

Industry/Entity Type

Hospitality and Tourism

Requirements
Must have
• Simplicity, luxe feel, eco-tourism
Nice to have
• Open to ideas/suggestions
Should not have
• Too much wording and imagery, hard to read font

```html
<!DOCTYPE html>
<html lang="en">
<head>
<meta charset="utf-8">
<title>The Wrenfield Tasmania — Landscape Advert</title>
<link rel="stylesheet" href="https://fonts.googleapis.com/css2?family=Marcellus&family=Archivo+Narrow:wght@400;700&display=swap">
<style>
  :root {
    --paper: #ffffff;
    --ink: #111111;
    --copper: #c98f5c;
    --rust: #a65a24;
    --sky-deep: #2f5a9a;
    --sky-gold: #f0dca0;
    --land-dark: #2c2a22;
    --sky-bright: #1f73d6;
    --sky-pale: #6cc0f5;
  }
  * { margin: 0; padding: 0; box-sizing: border-box; }
  html, body { width: 1200px; height: 846px; overflow: hidden; background: var(--paper); }
  .advert { position: relative; width: 1200px; height: 846px; background: var(--paper); overflow: hidden; }

  .photo { position: absolute; left: 0; width: 743px; }
  .photo--sunset-view {
    top: 0; height: 433px;
    background: linear-gradient(180deg, var(--sky-deep) 0%, #6f8db8 30%, var(--sky-gold) 58%, #7d7a66 68%, #45432f 80%, var(--land-dark) 100%);
  }
  .photo--pod {
    top: 433px; height: 413px;
    background: linear-gradient(180deg, var(--sky-bright) 0%, #3a98ef 45%, var(--sky-pale) 60%, #4a6a6e 72%, #3d4032 85%, #5c5446 100%);
  }

  .copy-panel {
    position: absolute; left: 743px; top: 0; width: 457px; height: 846px;
    text-align: center;
  }
  .brand-mark {
    position: absolute; left: 0; right: 0; top: 120px;
    display: flex; align-items: center; justify-content: center; gap: 10px;
    font-family: "Marcellus", serif; font-size: 30px; color: var(--rust);
    letter-spacing: 1px;
  }
  .brand-mark__dot { width: 14px; height: 14px; border-radius: 50%; background: var(--rust); }

  .headline {
    position: absolute; left: 0; right: 0; top: 288px;
    font-family: "Marcellus", serif; font-weight: 400;
    font-size: 35px; line-height: 41px; color: var(--ink);
    letter-spacing: 0.5px;
  }
  .tagline {
    position: absolute; left: 0; right: 0; top: 469px;
    font-family: "Archivo Narrow", sans-serif; font-size: 18px; line-height: 23px;
    color: var(--ink);
  }
  .cta {
    position: absolute; left: 118px; top: 579px; width: 228px; height: 39px;
    border: 1.5px solid var(--copper);
    display: flex; align-items: center; justify-content: center;
    font-family: "Archivo Narrow", sans-serif; font-weight: 700; font-size: 16px;
    color: var(--ink); letter-spacing: 0.3px; text-decoration: none;
  }
  .contact {
    position: absolute; left: 0; right: 0; top: 788px;
    font-family: "Archivo Narrow", sans-serif; font-size: 10.5px;
    letter-spacing: 0.6px; color: var(--ink);
  }

  .flourish { position: absolute; inset: 0; pointer-events: none; }
</style>
</head>
<body>
<main class="advert">
  <div class="photo photo--sunset-view" role="img" aria-label="Sunset view from Mount Halbrook over bushland, the Corvin River and distant hills under golden clouds"></div>
  <div class="photo photo--pod" role="img" aria-label="Dark metal-clad eco pod with a large window on a rocky hillside, sea and town below under a clear blue sky"></div>

  <svg class="flourish" viewBox="0 0 1200 846" width="1200" height="846" aria-hidden="true">
    <path d="M0,151 C130,190 240,255 305,335 C360,405 395,480 430,545 C475,615 570,662 700,656 C820,650 895,730 892,790 C890,815 880,832 870,846"
          fill="none" stroke="var(--copper)" stroke-width="1.6"/>
    <path d="M934,0 C965,30 1000,52 1049,50 C1090,48 1120,62 1140,95 C1160,125 1175,138 1200,139"
          fill="none" stroke="var(--copper)" stroke-width="1.6"/>
  </svg>

  <section class="copy-panel">
    <div class="brand-mark"><span class="brand-mark__dot"></span>The Wrenfield</div>
    <h1 class="headline">WHERE WILDERNESS<br>MEETS REFINED<br>COMFORT</h1>
    <p class="tagline">LUXURY PODS OVERLOOKING SEA,<br>RIVER &amp; SKY.</p>
    <a class="cta" href="https://www.thewrenfieldtasmania.example.com.au">DISCOVER THE WRENFIELD</a>
    <p class="contact">THEWRENFIELDTASMANIA.EXAMPLE.COM.AU | @THEWRENFIELDTAS</p>
  </section>
</main>
</body>
</html>
```